Infographics for Zelmora

Zelmora company specializes in providing services for the organization of low-budget crowdsourcing research.
Crowdsourcing research - the solution of the problem by lots of people on a competitive basis. Types of research will not be limited to the design competition, and will cover all areas of economic activity.

The site contains the following sections: directory of research, user communities, where they can organize the communication according to common interests, forum, news ticker.

The site will feature two groups of users:
1. Organizers of commercial research - the firm or individual businessmen
2. Researchers of commercial research. Moreover, the organizers can act as executors in the research organized by other users.

Motives Organizers of research:
1. Solving business problems quickly and inexpensively, and the variability of solutions.
2. The possibility of recruiting the best researchers.
3. Self-promotion (positioning your company as an innovative, using cutting-edge technology solutions).
4. Doing Business with the times.

The motives of researchers:
1. Earnings with their knowledge by participating in competitions and receive the prize fund.
2. Employability organized research (if the customer makes an offer the researcher).
3. Intelligent Leisure
4. Communication: forum, chat with the professionals of their field of study.

Required:
Graphically show the behavior of two groups of people based on their motives.
Schematically, the sheet should be divided into two parts - the left diagram of the model of the organizers, to the right - the researchers. The middle - it is desirable that part where the researchers will provide solutions to problems of the organizers - the scheme intersect each other graphically.
This work will be used for placement on the website of the company, as well as in printed promotional products.

Target Market(s)

Entrepreneurs, businesses as well as economically active population of Russia

Industry/Entity Type

Communication

Requirements
Must have
• The company's logo from the attached file.
All decals made with cursive. All decails are editable.
The source file in vector format EPS.
Nice to have
• The color scheme of the site will match the logo, so it is desirable that the figure used the same color as the logo: black, gray, green. In an attachment, "firm color" color settings in the CMYK.
Schemes must come from the top down, page orientation - portrait.
Should not have
• Do not use photos. Only pictures.

```html
<!DOCTYPE html>
<html lang="en">
<head>
<meta charset="utf-8">
<title>How can crowdsourcing help with your research? — Zelmora</title>
<link href="https://fonts.googleapis.com/css2?family=Josefin+Sans:wght@300;400;600&family=Quicksand:wght@400;500;600&family=Dancing+Script:wght@600;700&display=swap" rel="stylesheet">
<style>
  :root {
    --ink: #5b5f63;
    --ink-soft: #7a7e82;
    --green: #8dc63f;
    --green-pale: #eef4e3;
    --green-band: #d6e4bf;
    --green-box: #e1ebcf;
    --green-line: #a9c08a;
    --blue-pale: #e4f0f5;
    --blue-box: #d3e7ef;
    --blue-line: #7fc3d6;
    --teal: #2f9da4;
    --charcoal: #3f4244;
    --violet: #85509a;
    --coral: #e8584d;
    --white: #ffffff;
  }
  * { box-sizing: border-box; margin: 0; padding: 0; }
  html, body { width: 729px; height: 1200px; overflow: hidden; background: var(--white); }
  .sheet {
    position: relative; width: 612px; height: 1000px;
    transform: scale(1.1912, 1.2); transform-origin: 0 0;
    font-family: "Quicksand", sans-serif; color: var(--ink);
    background: linear-gradient(90deg, var(--green-pale) 0 50%, var(--blue-pale) 50% 100%);
  }
  .header { position: absolute; left: 0; top: 0; width: 612px; height: 103px;
    background: linear-gradient(180deg, #f4f8ec, #e8f0da); }
  .title { position: absolute; top: 24px; width: 100%; text-align: center;
    font-family: "Josefin Sans", sans-serif; font-weight: 400; color: var(--ink);
    line-height: 1.05; letter-spacing: 0.5px; }
  .title .small { font-size: 22px; }
  .title .big { font-size: 30px; }
  .band { position: absolute; left: 0; top: 104px; width: 612px; height: 30px;
    background: var(--green-band); display: flex; align-items: center; padding-left: 20px; }
  .brand { font-family: "Quicksand", sans-serif; font-weight: 600; font-size: 22px;
    color: var(--charcoal); display: flex; align-items: center; gap: 6px; }
  .brand .dot { width: 14px; height: 14px; border-radius: 50%; background: var(--green); }
  .band .tagline { margin-left: 22px; font-size: 9.6px; color: var(--ink); }
  .art { position: absolute; }
  .art-building { left: 22px; top: 148px; width: 108px; height: 100px;
    background: linear-gradient(180deg, #e2ecd2, #d3e2bd); opacity: .8; }
  .art-people { left: 448px; top: 150px; width: 142px; height: 82px;
    background: linear-gradient(180deg, #cfe6ef, #b9dbe7); opacity: .85; border-radius: 30px 30px 0 0; }
  .art-bulb { left: 38px; top: 436px; width: 190px; height: 270px;
    background: radial-gradient(ellipse at 50% 35%, #dfe9cc, #e8f0da 70%, transparent 72%); }
  .art-document { left: 384px; top: 452px; width: 196px; height: 262px;
    background: linear-gradient(180deg, #cfe4ee, #d9eaf1); opacity: .8; }
  .art-handshake { left: 282px; top: 777px; width: 48px; height: 48px; border-radius: 50%;
    background: radial-gradient(circle, #f1f1ee, #d9dcd6); border: 5px solid var(--charcoal); }
  .script { font-family: "Dancing Script", cursive; font-weight: 700; }
  .ribbon-label { position: absolute; font-size: 19px; }
  .label-organizers { left: 33px; top: 226px; color: var(--violet); }
  .label-researchers { left: 480px; top: 226px; color: var(--coral); }
  .label-crowd { position: absolute; left: 236px; top: 288px; width: 140px; text-align: center;
    font-size: 13px; color: var(--ink); transform: rotate(-4deg); }
  .bubble-text { position: absolute; text-align: center; font-size: 11.5px; line-height: 1.45; color: var(--ink); }
  .definition { left: 258px; top: 166px; width: 96px; }
  .motive { position: absolute; text-align: center; font-size: 11px; line-height: 1.5; padding: 10px 8px; color: var(--ink); white-space: nowrap; }
  .motive-org { left: 32px; top: 352px; width: 236px; height: 74px; background: var(--green-box); }
  .motive-res { left: 346px; top: 352px; width: 248px; height: 74px; background: var(--blue-box); }
  .hl-org { color: var(--violet); font-size: 12px; }
  .hl-res { color: var(--coral); font-size: 12px; }
  .hub-text { position: absolute; left: 246px; width: 120px; text-align: center; font-size: 12px; line-height: 1.45; color: var(--charcoal); white-space: nowrap; }
  .hub-top { top: 504px; }
  .hub-bottom { top: 596px; }
  .benefit-title { position: absolute; font-size: 18px; top: 714px; }
  .benefit-org { left: 64px; color: var(--violet); }
  .benefit-res { left: 404px; color: var(--coral); }
  .benefit { position: absolute; text-align: center; font-size: 11.5px; line-height: 1.45; padding: 8px 12px; color: var(--ink); white-space: nowrap; }
  .benefit.org { left: 52px; width: 222px; background: #e6eed7; }
  .benefit.res { left: 350px; width: 226px; background: #e6f1f5; }
  .b1 { top: 745px; height: 60px; }
  .b2 { top: 826px; height: 62px; }
  .footer { position: absolute; left: 0; top: 946px; width: 612px; height: 54px; background: var(--white);
    text-align: center; }
  .sections { margin-top: 12px; font-size: 10.5px; letter-spacing: .6px; color: var(--charcoal); font-weight: 500; }
  .footer .brand { justify-content: center; margin-top: 3px; font-size: 22px; }
  .lines { position: absolute; left: 0; top: 0; }
</style>
</head>
<body>
<div class="sheet">
  <div class="header">
    <h1 class="title"><span class="small">HOW CAN </span><span class="big">CROWDSOURCING</span><br><span class="small">HELP WITH YOUR </span><span class="big">RESEARCH</span><span class="small">?</span></h1>
  </div>
  <div class="band">
    <span class="brand"><span class="dot"></span>Zelmora</span>
    <span class="tagline">specializes in providing services for the organization of low-budget crowdsourcing research</span>
  </div>

  <div class="art art-building" role="img" aria-label="Line drawing of an office building"></div>
  <div class="art art-people" role="img" aria-label="Silhouettes of a group of researchers"></div>
  <div class="art art-bulb" role="img" aria-label="Faint lightbulb drawing"></div>
  <div class="art art-document" role="img" aria-label="Faint drawing of research documents"></div>

  <svg class="lines" width="612" height="1000" viewBox="0 0 612 1000" aria-hidden="true">
    <path d="M75 95 C50 40 110 8 210 8 L400 8 C500 8 560 40 535 95" fill="none" stroke="var(--green)" stroke-width="1.3" stroke-dasharray="4 3"/>
    <path d="M70 88 L75 97 L80 88" fill="none" stroke="var(--green)" stroke-width="1.3"/>
    <path d="M530 88 L535 97 L540 88" fill="none" stroke="var(--green)" stroke-width="1.3"/>
    <path d="M20 216 L236 216 L236 258 L20 258 L30 237 Z" fill="var(--green-band)"/>
    <path d="M592 216 L378 216 L378 258 L592 258 L582 237 Z" fill="var(--blue-box)"/>
    <path d="M220 290 Q306 266 392 290 L386 316 Q306 296 226 320 Z" fill="var(--green-band)"/>
    <circle cx="306" cy="205" r="72" fill="var(--white)" stroke="var(--teal)" stroke-width="8"/>
    <circle cx="306" cy="205" r="61" fill="none" stroke="#d6e8e9" stroke-width="2"/>
    <line x1="120" y1="258" x2="120" y2="352" stroke="var(--green-line)" stroke-dasharray="4 3"/>
    <line x1="490" y1="258" x2="490" y2="352" stroke="var(--blue-line)" stroke-dasharray="4 3"/>
    <line x1="306" y1="320" x2="306" y2="462" stroke="var(--ink-soft)" stroke-dasharray="4 3"/>
    <circle cx="306" cy="578" r="118" fill="var(--white)" stroke="var(--teal)" stroke-width="9"/>
    <circle cx="306" cy="578" r="108" fill="none" stroke="var(--charcoal)" stroke-width="14"/>
    <line x1="240" y1="578" x2="372" y2="578" stroke="var(--ink-soft)" stroke-dasharray="4 3"/>
    <path d="M200 496 Q218 486 236 492 L234 482 L256 500 L232 516 L234 505 Q218 500 204 510 Z" fill="var(--green)"/>
    <path d="M422 602 Q404 618 386 612 L386 601 L366 618 L388 636 L387 625 Q408 628 424 614 Z" fill="var(--teal)"/>
    <path d="M38 712 C20 650 80 640 110 680 C130 705 200 660 200 620" fill="none" stroke="var(--ink-soft)" stroke-dasharray="4 3"/>
    <path d="M574 712 C590 650 530 640 500 680 C480 705 410 660 410 620" fill="none" stroke="var(--ink-soft)" stroke-dasharray="4 3"/>
    <path d="M22 710 L292 710 L292 742 L22 742 L30 726 Z" fill="var(--green-band)"/>
    <path d="M590 710 L322 710 L322 742 L590 742 L582 726 Z" fill="var(--blue-box)"/>
    <line x1="95" y1="805" x2="95" y2="826" stroke="var(--green-line)" stroke-dasharray="4 3"/>
    <line x1="95" y1="815" x2="282" y2="815" stroke="var(--green-line)" stroke-dasharray="4 3"/>
    <line x1="520" y1="805" x2="520" y2="826" stroke="var(--blue-line)" stroke-dasharray="4 3"/>
    <line x1="330" y1="815" x2="520" y2="815" stroke="var(--blue-line)" stroke-dasharray="4 3"/>
  </svg>

  <p class="bubble-text definition">finding the solution of a problem by lots of people on a competitive basis</p>
  <p class="label-crowd script">Crowdsourcing research</p>
  <p class="ribbon-label script label-organizers">Organizers</p>
  <p class="ribbon-label script label-researchers">Researchers</p>

  <p class="motive motive-org">Need to solve business problems<br><span class="hl-org">quickly</span> and <span class="hl-org">inexpensively</span>,<br>with a variability of solutions.</p>
  <p class="motive motive-res">Make <span class="hl-res">earnings</span> from their <span class="hl-res">knowledge</span><br>by participating in competitions<br>and receiving the prize fund.</p>

  <p class="hub-text hub-top">possibility of<br>recruiting the best<br>researchers</p>
  <p class="hub-text hub-bottom">employable<br>organized research</p>

  <p class="benefit-title script benefit-org">Organizer Benefits</p>
  <p class="benefit-title script benefit-res">Researcher Benefits</p>
  <p class="benefit org b1">Position your company as<br><span class="hl-org">innovative</span>, using cutting-edge<br>technology solutions</p>
  <p class="benefit org b2"><span class="hl-org">Self promote</span> and do<br>business with the times</p>
  <p class="benefit res b1">Intelligent Leisure - earn<br><span class="hl-res">money</span> in your spare time</p>
  <p class="benefit res b2"><span class="hl-res">Communication</span>: forum, chat<br>with the professionals of their<br>field of study</p>

  <div class="art art-handshake" role="img" aria-label="Handshake between organizer and researcher"></div>

  <footer class="footer">
    <p class="sections">DIRECTORY OF RESEARCH • USER COMMUNITIES • FORUM • NEWS TICKER</p>
    <p class="brand"><span class="dot"></span>Zelmora</p>
  </footer>
</div>
</body>
</html>
```